RTW Vision and Core Values

We are wanting to promote our core values and vision on posters at our office. I have uploaded a copy of our logo. We would like to incorporate that, the vision and the core values. ALL THREE MUST BE INCLUDED ON THE DESIGN. For reference, our website is www.rtwpetroworks.com

Our vision is:
We are a Team of Power and Strength that Builds our People and Serves our Industry and Communities.

Our Values are:
We Operate with a Standard of Excellence.
We Do the Right Thing Every Time.
We Value and Recognize our People.
We are Team Players.
We Think and Act with Optimism and Faith.

```html
<!DOCTYPE html>
<html lang="en">
<head>
<meta charset="utf-8">
<title>RTW Vision and Core Values Poster</title>
<link href="https://fonts.googleapis.com/css2?family=Barlow+Semi+Condensed:wght@500;600;800&display=swap" rel="stylesheet">
<style>
  :root {
    --navy: #36445f;
    --blue: #2f86c8;
    --mid-blue: #33689a;
    --ink: #111418;
    --paper: #ffffff;
    --stage: #e2e2e2;
    --steel-light: #e8ebef;
    --steel-dark: #8c96a3;
  }
  * { margin: 0; padding: 0; box-sizing: border-box; }
  html, body { width: 1200px; height: 1200px; overflow: hidden; }
  body {
    background: var(--stage);
    font-family: "Barlow Semi Condensed", sans-serif;
    position: relative;
  }
  .poster {
    position: absolute;
    left: 152px;
    top: 20px;
    width: 895px;
    height: 1160px;
    background: var(--paper);
    overflow: hidden;
  }
  .vision-band {
    position: absolute;
    left: 0;
    top: 58px;
    width: 855px;
    height: 99px;
    background: linear-gradient(90deg, var(--navy), var(--blue));
  }
  .band-stripes {
    position: absolute;
    left: 863px;
    top: 58px;
    width: 28px;
    height: 99px;
    background: linear-gradient(90deg,
      var(--blue) 0 5px, transparent 5px 11px,
      var(--blue) 11px 16px, transparent 16px 22px,
      var(--blue) 22px 27px, transparent 27px);
  }
  .heading {
    position: absolute;
    left: 65px;
    font-weight: 800;
    font-size: 96px;
    line-height: 1;
    letter-spacing: 1px;
  }
  .vision-heading { top: 63px; color: var(--paper); }
  .values-heading {
    top: 310px;
    background: linear-gradient(90deg, var(--navy), var(--blue) 85%);
    -webkit-background-clip: text;
    background-clip: text;
    color: transparent;
  }
  .vision-text {
    position: absolute;
    left: 65px;
    top: 195px;
    width: 800px;
    font-weight: 500;
    font-size: 32px;
    line-height: 40px;
    color: var(--ink);
  }
  .values-graphic { position: absolute; left: 0; top: 0; }
  .value {
    position: absolute;
    font-weight: 500;
    font-size: 29px;
    line-height: 1;
    color: var(--ink);
    white-space: nowrap;
  }
  .footer-band {
    position: absolute;
    left: 0;
    top: 1068px;
    width: 612px;
    height: 92px;
    background: linear-gradient(180deg, #4a6286, var(--navy));
    clip-path: polygon(0 0, 588px 0, 612px 100%, 0 100%);
  }
  .truck-photo {
    position: absolute;
    left: 12px;
    top: 950px;
    width: 550px;
    height: 196px;
    border-radius: 30px 60px 20px 20px;
    background: linear-gradient(180deg, var(--steel-light), var(--steel-dark));
  }
  .brand {
    position: absolute;
    left: 636px;
    top: 960px;
    width: 220px;
    text-align: center;
  }
  .brand-dot {
    width: 70px;
    height: 70px;
    margin: 0 auto 14px;
    border-radius: 50%;
    background: var(--mid-blue);
  }
  .brand-name {
    font-weight: 800;
    font-size: 66px;
    line-height: 1;
    color: var(--mid-blue);
    letter-spacing: 4px;
  }
</style>
</head>
<body>
  <main class="poster">
    <div class="vision-band"></div>
    <div class="band-stripes"></div>
    <h1 class="heading vision-heading">OUR VISION</h1>
    <p class="vision-text">We are a Team of Power and Strength that Builds our People and Serves our Industry and Communities</p>

    <h2 class="heading values-heading">OUR VALUES</h2>

    <svg class="values-graphic" width="895" height="1160" viewBox="0 0 895 1160" aria-hidden="true">
      <defs>
        <linearGradient id="arc-stroke" x1="0" y1="0" x2="0" y2="1">
          <stop offset="0" stop-color="#36445f"/>
          <stop offset="0.5" stop-color="#2f86c8"/>
          <stop offset="1" stop-color="#36445f"/>
        </linearGradient>
        <radialGradient id="icon-fill" cx="0.35" cy="0.3" r="0.8">
          <stop offset="0" stop-color="#3f7fbd"/>
          <stop offset="1" stop-color="#2c4466"/>
        </radialGradient>
      </defs>
      <path d="M111 425 A259 259 0 0 1 111 943" fill="none" stroke="url(#arc-stroke)" stroke-width="2.5"/>
      <g stroke="#fff" stroke-width="1.6" fill="none" stroke-linejoin="round" stroke-linecap="round">
        <!-- excellence: diamond -->
        <circle cx="264" cy="477" r="18" fill="url(#icon-fill)" stroke="none"/>
        <path d="M254 473 L259 467 H269 L274 473 L264 487 Z M254 473 H274 M259 467 L264 473 L269 467"/>
        <!-- right thing: thumbs up -->
        <circle cx="346" cy="577" r="18" fill="url(#icon-fill)" stroke="none"/>
        <path d="M337 575 h4 v11 h-4 Z M341 576 l5 -8 q2 -3 3 1 l-1 5 h6 q2 0 1.5 2.5 l-2 7 q-0.5 2 -2.5 2 h-10"/>
        <!-- people: person -->
        <circle cx="369" cy="684" r="18" fill="url(#icon-fill)" stroke="none"/>
        <circle cx="369" cy="679" r="4"/>
        <path d="M360 692 q9 -10 18 0 Z"/>
        <!-- optimism and faith: heart in hands -->
        <circle cx="345" cy="795" r="18" fill="url(#icon-fill)" stroke="none"/>
        <path d="M345 792 q-5 -6 -8 -2 q-2 4 8 10 q10 -6 8 -10 q-3 -4 -8 2 Z"/>
        <path d="M334 794 v6 l5 5 M356 794 v6 l-5 5"/>
        <!-- team players: group -->
        <circle cx="267" cy="890" r="18" fill="url(#icon-fill)" stroke="none"/>
        <circle cx="267" cy="885" r="3"/>
        <circle cx="259" cy="888" r="2.5"/>
        <circle cx="275" cy="888" r="2.5"/>
        <path d="M261 897 q6 -8 12 0 M254 896 q3 -5 7 -3 M280 896 q-3 -5 -7 -3"/>
      </g>
    </svg>

    <p class="value" style="left:305px; top:462px;">We Operate with a Standard of Excellence</p>
    <p class="value" style="left:378px; top:562px;">We Do the Right Thing Every Time</p>
    <p class="value" style="left:400px; top:669px;">We Value and Recognize our People.</p>
    <p class="value" style="left:371px; top:780px;">We Think and Act with Optimism and Faith</p>
    <p class="value" style="left:305px; top:875px;">We are Team Players</p>

    <div class="footer-band"></div>
    <div class="truck-photo" role="img" aria-label="Photo of a silver RTW vacuum tanker truck"></div>

    <div class="brand">
      <div class="brand-dot"></div>
      <p class="brand-name">RTW</p>
    </div>
  </main>
</body>
</html>
```